Wanderlark Gin - Bottle Label for a craft Gin about to be launched on the world from New Zealand

We are a start up craft distillery in New Zealand. We have developed a wonderful Gin using our own grain spirit and both traditional and New Zealand native botanicals (Manuka to be specific), chosen our bottle and the name "Wanderlark" and done a bit of amateur label design and now we are looking for someone to make it great.

Feel free to change up our amateur concept but give us something that will pop from the back bar and scream authenticity, craft and individuality.

The attached files give you the specifications of the bottle, our current concept for a Wanderlark label and an earlier concept drawing that gives an idea of where we are thinking the two labels should go on the front of the bottle.

Thanks, we look forward to your ideas!!

Target Market(s)

High end and craft Gin drinkers. Hipsters and cocktail barflys and their bar tenders and bar owners

Requirements
Must have
• Attractive individuality
Nice to have
• Coolness
Should not have
• Uncoolness

```html
<!DOCTYPE html>
<html lang="en">
<head>
<meta charset="utf-8">
<title>Wanderlark Gin – Bottle Label</title>
<link rel="stylesheet" href="https://fonts.googleapis.com/css2?family=Yesteryear&display=swap">
<style>
  :root {
    --paper: #ffffff;
    --ink: #111111;
    --navy: #1c1f4a;
    --leaf: #2f9a3a;
  }
  * { margin: 0; padding: 0; box-sizing: border-box; }
  html, body {
    width: 1200px;
    height: 1200px;
    overflow: hidden;
    background: var(--paper);
  }
  .canvas {
    position: relative;
    width: 1200px;
    height: 1200px;
    background: var(--paper);
  }
  .band {
    position: absolute;
    left: 280px;
    width: 640px;
  }
  .band--black { background: var(--ink); height: 22px; }
  .band--green { background: var(--leaf); height: 12px; }
  .band--top-black { top: 390px; }
  .band--top-green { top: 416px; }
  .band--bottom-green { top: 810px; }
  .band--bottom-black { top: 828px; height: 18px; }

  .brand-name {
    position: absolute;
    top: 470px;
    left: 280px;
    width: 640px;
    text-align: center;
    font-family: "Yesteryear", cursive;
    font-weight: 400;
    font-size: 124px;
    line-height: 1.1;
    color: var(--ink);
  }
  .tagline {
    position: absolute;
    top: 664px;
    left: 280px;
    width: 640px;
    text-align: center;
    font-family: "Yesteryear", cursive;
    font-size: 50px;
    line-height: 1;
    color: var(--navy);
  }
  .story {
    position: absolute;
    top: 918px;
    left: 360px;
    width: 480px;
    text-align: center;
    font-family: "Yesteryear", cursive;
    font-size: 37px;
    line-height: 48px;
    color: var(--ink);
  }
</style>
</head>
<body>
<main class="canvas">
  <div class="band band--black band--top-black"></div>
  <div class="band band--green band--top-green"></div>

  <h1 class="brand-name">Wanderlark</h1>
  <p class="tagline">New Zealand small batch Gin</p>

  <div class="band band--green band--bottom-green"></div>
  <div class="band band--black band--bottom-black"></div>

  <p class="story">
    A classically inspired Gin<br>
    with developed citrus notes from<br>
    the Manuka berries from<br>
    Callum’s mates. Best with an<br>
    equal mix of some fancy tonic.
  </p>
</main>
</body>
</html>
```